Medical Billing and Professional Services

We are a full-service medical billing company, utilizing state-of-the art software to analyze, code, and electronically bill commercial and government subsidized insurance companies for physicians' services provided to patients. We bill both hospital and private clinics' claims directly to the appropriate carrier, with reduced turn-around times, increased cash flow, and greater profitability to the physician or practice. We customize every client's pricing to their specific practice, and the services they might require. Generally, we operate on a percentage basis of the allowed charges for particular procedure, but also can arrange monthly or per claim pricing. We can manage A/R, and work with a collection company that goes after delinquents. WE ARE NOT A COLLECTION AGENCY, and do not represent ourselves as such. However, our company practices do eliminate much of the need for such.
We follow up, follow up, and follow up until a claim is paid in full, according to contractual schedules. We also eliminate the practice's need to spend hours on the phone to resolve unpaid claims, thus reducing labor, equipment, and computer costs. In essence, more money to the bottom line for the practice.
However, we almost never gain a client without a meeting. There are many online services, but our strength is personal relationship. The owner ALWAYS meets with the doctors or office manager. Our success depends on getting the practice paid in full for their services. (Which we do 99.2% of the time).
We also offer notary service, when needed.

Target Market(s)

physicians in private practice, also chiropractors, and doctors not employed by hospitals or clinics.

Industry/Entity Type

Government

Requirements
Must have
• attractive colors, basic information about the benefits of using a billing service.. Call to action is very important. Our reach out in the past has been: "You care for your patients, WE care for your practice."
Nice to have
• focus on electronics and new technology, which we have. Also our reputation with current clients, and 12 years of experience.
Should not have
• no old fonts, money icons or references to gold or money.

```html
<!DOCTYPE html>
<html lang="en">
<head>
<meta charset="utf-8">
<title>Northgate Medical Billing Center – Postcard</title>
<link rel="stylesheet" href="https://fonts.googleapis.com/css2?family=Open+Sans:wght@400;600;700&family=PT+Sans+Narrow:wght@400&family=Dancing+Script:wght@500&display=swap">
<style>
  :root {
    --stage: #575757;
    --paper: #ffffff;
    --green: #1ba57c;
    --green-light: #2bb98d;
    --green-dark: #12916a;
    --ink: #111111;
    --text-dark: #222222;
    --yellow: #f4e13a;
    --photo-a: #d9dcdc;
    --photo-b: #8f9697;
  }
  * { box-sizing: border-box; margin: 0; padding: 0; }
  html, body { width: 1200px; height: 500px; overflow: hidden; }
  body { background: var(--stage); font-family: "Open Sans", Arial, sans-serif; position: relative; }

  .card { position: absolute; top: 31px; height: 434px; overflow: hidden; background: var(--paper); }

  /* ---------- Front ---------- */
  .card--front { left: 35px; width: 557px; background: var(--green); }
  .front__green { position: absolute; inset: 0; background: linear-gradient(160deg, var(--green-dark) 0%, var(--green) 45%, var(--green-light) 100%); }
  .front__header { position: absolute; left: 0; top: 0; width: 557px; height: 130px; }
  .brand { position: absolute; display: flex; align-items: flex-start; gap: 10px; color: var(--ink); font-weight: 400; }
  .brand__mark { background: var(--green); border-radius: 6px; flex: none; }
  .brand__text { display: flex; flex-direction: column; }
  .brand__name { line-height: 1; letter-spacing: 1px; }
  .brand__full { line-height: 1.1; }

  .card--front .brand { left: 22px; top: 12px; }
  .card--front .brand__mark { width: 70px; height: 70px; margin-top: 4px; }
  .card--front .brand__name { font-size: 42px; }
  .card--front .brand__full { font-size: 11.5px; margin-top: 6px; text-transform: uppercase; }

  .photo-laptop { position: absolute; left: 332px; top: 20px; width: 212px; height: 272px; border-radius: 10px;
    background: linear-gradient(150deg, var(--photo-a) 0%, #b9bebf 45%, var(--photo-b) 100%); }

  .benefits { position: absolute; left: 19px; top: 130px; color: var(--paper); }
  .benefits__title { font-size: 19px; font-weight: 600; margin-bottom: 8px; }
  .benefits__list { list-style: none; }
  .benefits__item { display: flex; align-items: center; gap: 12px; font-size: 15px; height: 29px; }
  .tick { width: 14px; height: 14px; flex: none; }

  .tagline { position: absolute; right: 18px; top: 305px; text-align: right; color: var(--yellow);
    font-family: "Dancing Script", cursive; font-size: 20px; line-height: 1.25; }

  .call-bar { position: absolute; left: 0; bottom: 0; width: 100%; height: 60px; background: var(--ink);
    color: var(--paper); font-weight: 700; font-size: 24px; display: flex; align-items: center; justify-content: center; }

  /* ---------- Back ---------- */
  .card--back { left: 609px; width: 566px; }
  .back__panel { position: absolute; left: 0; top: 0; width: 261px; height: 100%; }
  .back__header { position: absolute; left: 0; top: 0; width: 261px; height: 90px; background: var(--paper); border-bottom: 3px solid #333; }
  .card--back .brand { left: 12px; top: 16px; gap: 8px; }
  .card--back .brand__mark { width: 42px; height: 42px; margin-top: 2px; }
  .card--back .brand__name { font-size: 28px; }
  .card--back .brand__full { font-size: 12px; margin-top: 4px; }

  .back__green { position: absolute; left: 0; top: 90px; width: 261px; bottom: 0;
    background: radial-gradient(ellipse at 60% 45%, var(--green-light) 0%, var(--green) 55%, var(--green-dark) 100%); }
  .offer { position: absolute; left: 0; top: 108px; width: 261px; text-align: center; color: var(--yellow); font-size: 13.5px; line-height: 1.35; }
  .offer__big { font-size: 27px; line-height: 1; }
  .more-info { position: absolute; left: 0; top: 190px; width: 261px; text-align: center; color: var(--paper); }
  .more-info__label { font-size: 12.5px; }
  .more-info__url { font-size: 16px; margin-top: 6px; }
  .more-info__or { font-size: 16px; margin-top: 4px; }

  .back__call { position: absolute; left: 2px; top: 276px; width: 252px; height: 85px; background: var(--ink);
    color: var(--paper); font-weight: 700; text-align: center; display: flex; flex-direction: column; justify-content: center; gap: 4px; }
  .back__call-label { font-size: 19px; }
  .back__call-phone { font-size: 23px; }

  .contact { position: absolute; left: 268px; top: 14px; font-family: "PT Sans Narrow", "Arial Narrow", sans-serif; font-size: 15px; line-height: 24px; color: var(--text-dark); white-space: nowrap; }
  .contact__label { color: var(--green); }
  .stamp { position: absolute; left: 430px; top: 17px; width: 119px; height: 118px; border: 1.5px solid var(--ink); }
  .address-lines { position: absolute; left: 288px; top: 214px; width: 262px; }
  .address-lines__line { height: 2px; background: var(--ink); margin-bottom: 37.5px; }
</style>
</head>
<body>

<section class="card card--front">
  <div class="front__green"></div>
  <svg class="front__header" viewBox="0 0 557 130" aria-hidden="true">
    <path d="M0 0 H557 V4 C470 20 380 70 300 96 C220 118 120 122 0 120 Z" fill="#ffffff"/>
    <path d="M300 96 C380 70 470 20 557 4 V14 C470 34 390 78 300 96 Z" fill="#111111"/>
    <path d="M520 0 H557 V4 C545 7 532 10 520 14 Z" fill="#111111"/>
  </svg>

  <div class="photo-laptop" role="img" aria-label="Photo of an open laptop with a red stethoscope lying on its keyboard"></div>

  <div class="brand">
    <div class="brand__mark"></div>
    <div class="brand__text">
      <span class="brand__name">NMBC</span>
      <span class="brand__full">Northgate Medical Billing Center</span>
    </div>
  </div>

  <div class="benefits">
    <h2 class="benefits__title">WHY CHOOSE NMBC?</h2>
    <ul class="benefits__list">
      <li class="benefits__item"><svg class="tick" viewBox="0 0 14 14"><path d="M1 7.5 L5 11.5 L13 2" fill="none" stroke="#fff" stroke-width="2"/></svg>Saves Labor Cost</li>
      <li class="benefits__item"><svg class="tick" viewBox="0 0 14 14"><path d="M1 7.5 L5 11.5 L13 2" fill="none" stroke="#fff" stroke-width="2"/></svg>Saves Time</li>
      <li class="benefits__item"><svg class="tick" viewBox="0 0 14 14"><path d="M1 7.5 L5 11.5 L13 2" fill="none" stroke="#fff" stroke-width="2"/></svg>Experienced Staff</li>
      <li class="benefits__item"><svg class="tick" viewBox="0 0 14 14"><path d="M1 7.5 L5 11.5 L13 2" fill="none" stroke="#fff" stroke-width="2"/></svg>State-of-the Art Software</li>
      <li class="benefits__item"><svg class="tick" viewBox="0 0 14 14"><path d="M1 7.5 L5 11.5 L13 2" fill="none" stroke="#fff" stroke-width="2"/></svg>Certified Coders and Billing Specialists</li>
      <li class="benefits__item"><svg class="tick" viewBox="0 0 14 14"><path d="M1 7.5 L5 11.5 L13 2" fill="none" stroke="#fff" stroke-width="2"/></svg>We follow up until you get paid.</li>
    </ul>
  </div>

  <p class="tagline">You care for your patients,<br>WE care for your practice.</p>

  <div class="call-bar">CALL US TODAY: 555-014-2290</div>
</section>

<section class="card card--back">
  <div class="back__panel">
    <div class="back__header"></div>
    <div class="brand">
      <div class="brand__mark"></div>
      <div class="brand__text">
        <span class="brand__name">NMBC</span>
        <span class="brand__full">Northgate Medical Billing Center</span>
      </div>
    </div>
    <div class="back__green"></div>
    <p class="offer"><span class="offer__big">25%</span> off any service for 3 months,<br>or first month's services for free with<br>1 year contract</p>
    <div class="more-info">
      <p class="more-info__label">For More Information Visit</p>
      <p class="more-info__url">www.example.com</p>
      <p class="more-info__or">or</p>
    </div>
    <div class="back__call">
      <span class="back__call-label">CALL US TODAY</span>
      <span class="back__call-phone">555-014-2290</span>
    </div>
  </div>

  <div class="contact">
    <p><span class="contact__label">Ph:</span> 555-014-2290</p>
    <p><span class="contact__label">Fax:</span> 555-019-3371</p>
    <p><span class="contact__label">Email:</span> nmbc01@example.com</p>
  </div>
  <div class="stamp"></div>
  <div class="address-lines">
    <div class="address-lines__line"></div>
    <div class="address-lines__line"></div>
    <div class="address-lines__line"></div>
    <div class="address-lines__line"></div>
  </div>
</section>

</body>
</html>
```